Bakery looking for new Business cards

I have a new logo and now its time to upgrade our business cards.
e-mail - info@corwelbakehouse.com
www.corwelbakehouse.com
318-547-2096

418e Pell Creek rd. Brackenford IL 60219
Bakery Hour's Tuesday-Saturday 8am-5pm

Industry/Entity Type

Bakery

Contact Information for Business Card

Hr's

Requirements
Must have
• Business information.
Nice to have
• would like to include a QR code for our website.

```html
<!DOCTYPE html>
<html lang="en">
<head>
<meta charset="utf-8">
<title>Corwel's bakery – business cards</title>
<link href="https://fonts.googleapis.com/css2?family=Poppins:wght@400;500;600&display=swap" rel="stylesheet">
<style>
  :root {
    --page: #e9ecf1;
    --card: #ffffff;
    --ink: #1d1d1d;
    --gold: #e2a93b;
    --pattern: #f1f1f1;
    --shadow: rgba(20, 30, 50, 0.18);
  }
  html, body {
    margin: 0;
    width: 1200px;
    height: 800px;
    overflow: hidden;
    background: var(--page);
    font-family: "Poppins", sans-serif;
    color: var(--ink);
  }
  .canvas {
    position: relative;
    width: 1200px;
    height: 800px;
  }
  .card {
    position: absolute;
    width: 525px;
    height: 300px;
    background: var(--card);
    box-shadow: 0 10px 28px var(--shadow);
    overflow: hidden;
  }
  .card--front { left: 60px; top: 80px; }
  .card--back { left: 615px; top: 420px; }

  .dessert-pattern {
    position: absolute;
    inset: 0;
    background: linear-gradient(135deg, var(--pattern), #fbfbfb 75%);
  }
  .web-band {
    position: absolute;
    left: 455px; top: 22px;
    width: 32px; height: 240px;
    background: var(--gold);
  }
  .web-band__text {
    position: absolute;
    left: 50%; top: 50%;
    transform: translate(-50%, -50%) rotate(90deg);
    white-space: nowrap;
    color: #fff;
    font-size: 14px;
    letter-spacing: 0.6px;
  }
  .brand {
    position: absolute;
    display: flex;
    align-items: center;
    gap: 12px;
  }
  .brand--front { left: 40px; top: 170px; }
  .brand--back { left: 40px; top: 226px; }
  .brand__dot {
    width: 30px; height: 30px;
    border-radius: 50%;
    background: var(--gold);
  }
  .brand__name {
    font-weight: 500;
    font-size: 26px;
    line-height: 1;
  }
  .brand--back .brand__name { font-size: 21px; }
  .brand__tagline {
    margin-top: 4px;
    font-size: 14px;
    letter-spacing: 0.5px;
    color: var(--gold);
  }
  .brand--back .brand__tagline { font-size: 12px; }

  .contact-band {
    position: absolute;
    left: 70px; top: 0;
    width: 30px; height: 160px;
    background: var(--gold);
  }
  .contact-icons {
    position: absolute;
    left: 76px; top: 66px;
    display: flex;
    flex-direction: column;
    gap: 8px;
  }
  .contact-list {
    position: absolute;
    left: 118px; top: 56px;
    margin: 0; padding: 0;
    list-style: none;
    font-size: 14px;
    line-height: 26px;
  }
  .address {
    position: absolute;
    right: 40px; top: 168px;
    font-style: normal;
    font-size: 13px;
    line-height: 20px;
  }
</style>
</head>
<body>
<main class="canvas">
  <section class="card card--front">
    <div class="dessert-pattern" role="img" aria-label="Faint line drawings of cakes, cupcakes and hearts"></div>
    <div class="brand brand--front">
      <span class="brand__dot"></span>
      <div>
        <div class="brand__name">Corwel's bakery</div>
        <div class="brand__tagline">DESSERT SHOP</div>
      </div>
    </div>
    <div class="web-band"><span class="web-band__text">www.corwelbakehouse.com</span></div>
  </section>

  <section class="card card--back">
    <div class="contact-band"></div>
    <div class="contact-icons">
      <svg width="18" height="18" viewBox="0 0 24 24" aria-label="Phone"><path fill="#1d1d1d" d="M6.6 10.8a15 15 0 0 0 6.6 6.6l2.2-2.2a1 1 0 0 1 1-.25 11.4 11.4 0 0 0 3.6.57 1 1 0 0 1 1 1V20a1 1 0 0 1-1 1A17 17 0 0 1 3 4a1 1 0 0 1 1-1h3.5a1 1 0 0 1 1 1c0 1.25.2 2.45.57 3.6a1 1 0 0 1-.25 1z"/></svg>
      <svg width="18" height="18" viewBox="0 0 24 24" aria-label="Email"><path fill="#1d1d1d" d="M3 5h18v14H3z"/><path fill="none" stroke="#e2a93b" stroke-width="1.6" d="M3 6l9 7 9-7"/></svg>
      <svg width="18" height="18" viewBox="0 0 24 24" aria-label="Website"><path fill="#1d1d1d" d="M4 4l15 6-6 2-2 6z"/><path stroke="#1d1d1d" stroke-width="2.4" d="M13 13l7 7"/></svg>
    </div>
    <ul class="contact-list">
      <li>318-547-2096</li>
      <li>info@corwelbakehouse.com</li>
      <li>www.corwelbakehouse.com</li>
    </ul>
    <address class="address">418e Pell Creek rd.<br>Brackenford IL 60219</address>
    <div class="brand brand--back">
      <span class="brand__dot"></span>
      <div>
        <div class="brand__name">Corwel's bakery</div>
        <div class="brand__tagline">DESSERT SHOP</div>
      </div>
    </div>
  </section>
</main>
</body>
</html>
```